Reaching the Root: Reasoning in Clinical Choice-Making

I'd like a cover that looks like it would fit on the shelf next to "The Symptom Mirage" by Harold Vintner, "The Fall of Forgetting" by Carl Mortenson, "Meal Mend" by Neil Forsby, "The Energy Renewal Plan" by Owen Prichardson or "The Gland Renewal Plan" by the same or "The Cortex Renewal Plan" by the same ... either text only (with some interesting fonts that make the title stand out, and the subtitle smaller) or a relevant image, though I'm not entirely sure what that would be since this is a book about big-picture medical decision making.
Author name is Dr Miriam Oakhurst, NMD
I'll eventually request an e-book, paperback, and audio cover from the winner...

Target Market(s)

practicing physicians

Industry/Entity Type

medicine

Requirements
Must have
• look similar to other books in the genre

```html
<!DOCTYPE html>
<html lang="en">
<head>
<meta charset="utf-8">
<title>Reaching the Root: Reasoning in Clinical Choice-Making</title>
<link rel="stylesheet" href="https://fonts.googleapis.com/css2?family=Crimson+Pro:wght@700&family=Poppins:wght@200;400&display=swap">
<style>
  :root {
    --bg-core: #1d3d6c;
    --bg-mid: #292c6a;
    --bg-edge: #22235a;
    --title-white: #ffffff;
    --gold: #b58d40;
    --teal: #2ea6b2;
  }
  html, body {
    margin: 0;
    padding: 0;
    overflow: hidden;
    background: var(--bg-edge);
  }
  .cover {
    position: relative;
    width: 800px;
    height: 1200px;
    overflow: hidden;
    background: radial-gradient(ellipse at 50% 58%, var(--bg-core) 0%, var(--bg-mid) 55%, var(--bg-edge) 100%);
  }
  .cover-art {
    position: absolute;
    inset: 0;
    width: 800px;
    height: 1200px;
  }
  .title-main {
    font-family: "Crimson Pro", Georgia, serif;
    font-weight: 700;
  }
  .title-top { fill: var(--title-white); }
  .title-joiner, .title-key { fill: var(--gold); }
  .joiner-rule { stroke: var(--gold); stroke-width: 2.5; }
  .subtitle {
    font-family: "Poppins", Arial, sans-serif;
    font-weight: 200;
    fill: var(--title-white);
  }
  .author {
    font-family: "Poppins", Arial, sans-serif;
    font-weight: 400;
    fill: var(--teal);
  }
  .author-rule { stroke: var(--teal); stroke-width: 3; }
</style>
</head>
<body>
  <main class="cover">
    <svg class="cover-art" viewBox="0 0 800 1200" xmlns="http://www.w3.org/2000/svg">
      <defs>
        <radialGradient id="emblemTone" cx="50%" cy="50%" r="50%">
          <stop offset="0%" stop-color="#2ea6b2" stop-opacity="0.55"/>
          <stop offset="70%" stop-color="#2ea6b2" stop-opacity="0.35"/>
          <stop offset="100%" stop-color="#2ea6b2" stop-opacity="0.15"/>
        </radialGradient>
      </defs>

      <text class="title-main title-top" x="92" y="159" font-size="138" textLength="618" lengthAdjust="spacingAndGlyphs">REACHING</text>

      <line class="joiner-rule" x1="95" y1="228" x2="300" y2="228"/>
      <text class="title-main title-joiner" x="400" y="253" font-size="66" text-anchor="middle">THE</text>
      <line class="joiner-rule" x1="500" y1="228" x2="705" y2="228"/>

      <text class="title-main title-key" x="89" y="468" font-size="246" textLength="622" lengthAdjust="spacingAndGlyphs">ROOT</text>

      <text class="subtitle" x="400" y="540" font-size="47" text-anchor="middle">REASONING IN</text>
      <text class="subtitle" x="400" y="597" font-size="47" text-anchor="middle">CLINICAL</text>
      <text class="subtitle" x="400" y="655" font-size="47" text-anchor="middle">CHOICE-MAKING</text>

      <g role="img" aria-label="Teal line emblem of a circular maze with an arrow leading up out of its centre">
        <circle cx="400" cy="852" r="114" fill="url(#emblemTone)"/>
      </g>

      <text class="author" x="400" y="1104" font-size="42" text-anchor="middle" textLength="527" lengthAdjust="spacingAndGlyphs">DR MIRIAM OAKHURST, NMD</text>
      <line class="author-rule" x1="67" y1="1131" x2="733" y2="1131"/>
    </svg>
  </main>
</body>
</html>
```